Business Card Design and Basic Text Logo

We are looking for a business card design for an e-business company. Our business is the parent company of a few website businesses. The final logo and business card design will communicate a conservative but modern and expansive business

The Logo text is: 87Merchant
We would also like a basic text logo design for 87Merchant. The logo could also fill up the reverse side of the business card.

The colours we would like to use are:
White
Navy
Black

This is the text that will be added to the card:

Dean Colley
Business Development Manager

Phone: +61 417 658 294
Email: dean.colley@87merchant.com.au

Industry/Entity Type

Business

Logo Text

87Merchant

Logo styles of interest
Pictorial/Combination Logo
Requirements
Must have
• Modern and attractive design
Nice to have
• communicate a conservative but modern and expansive business
Should not have
• Should be too dull and plan
• But also should be overly colourful

```html
<!DOCTYPE html>
<html lang="en">
<head>
<meta charset="utf-8">
<title>87Merchant Business Card</title>
<link rel="stylesheet" href="https://fonts.googleapis.com/css2?family=Oxygen:wght@300;400;700&display=swap">
<style>
  :root {
    --navy: #07005a;
    --white: #ffffff;
    --ink: #000000;
    --edge: #444444;
  }
  html, body {
    margin: 0;
    padding: 0;
    overflow: hidden;
  }
  body {
    width: 900px;
    height: 1200px;
    background: var(--white);
    position: relative;
    font-family: "Oxygen", "Helvetica Neue", Arial, sans-serif;
  }
  .card {
    position: absolute;
    left: 126px;
    width: 663px;
    height: 405px;
    border: 1px solid var(--edge);
    background: var(--white);
    overflow: hidden;
    box-sizing: content-box;
  }
  .card--front { top: 141px; }
  .card--back  { top: 614px; }

  /* Front: name with plain square */
  .brand-square {
    position: absolute;
    left: 19px;
    top: 196px;
    width: 110px;
    height: 110px;
    background: var(--navy);
  }
  .brand-name {
    position: absolute;
    left: 150px;
    top: 200px;
    margin: 0;
    font-weight: 300;
    font-size: 80px;
    line-height: 1;
    letter-spacing: -1px;
    color: var(--navy);
    white-space: nowrap;
  }

  /* Back: contact details */
  .contact {
    position: absolute;
    left: 33px;
    top: 226px;
    margin: 0;
    font-weight: 700;
    font-size: 21px;
    font-variant: small-caps;
    line-height: 30px;
    color: var(--ink);
  }
  .contact p { margin: 0; }
  .contact .gap { height: 32px; }

  /* Back: navy band with vertical name */
  .band {
    position: absolute;
    right: 0;
    top: 0;
    width: 152px;
    height: 100%;
    background: var(--navy);
  }
  .band-name {
    position: absolute;
    left: 50%;
    top: 50%;
    transform: translate(-50%, -50%) rotate(-90deg);
    margin: 0;
    font-weight: 300;
    font-size: 58px;
    line-height: 1;
    color: var(--white);
    white-space: nowrap;
  }
</style>
</head>
<body>
  <section class="card card--front" aria-label="Card front">
    <div class="brand-square"></div>
    <h1 class="brand-name">87Merchant</h1>
  </section>

  <section class="card card--back" aria-label="Card back">
    <div class="contact">
      <p>Dean Colley</p>
      <p>Business Development Manager</p>
      <div class="gap"></div>
      <p>Phone: +61 417 658 294</p>
      <p>Email: dean.colley@87merchant.com.au</p>
    </div>
    <div class="band">
      <p class="band-name">87Merchant</p>
    </div>
  </section>
</body>
</html>
```